Solution Matrix for our Company

Develop an image that describes our "4 solutions". We eventually will list the products and services we have that address the solution being discussed. Our main website is http://brightlane4jobs.example/. Feel free to look through the material there as well as the material we are addressing.

The mock document is a summary of the 4 solution buckets. We have also attached some samples from states that have done similar work. Feel free to be creative and use graphics and/or pictures in your design

Target Market(s)

Education

```html
<!DOCTYPE html>
<html lang="en">
<head>
<meta charset="utf-8">
<title>B4J Career Readiness Model</title>
<link href="https://fonts.googleapis.com/css2?family=Roboto+Condensed:wght@300;700&family=Roboto:wght@400;500&display=swap" rel="stylesheet">
<style>
  :root{
    --red:#e4430f;
    --orange:#f7941d;
    --orange-deep:#e8561a;
    --grey:#58585a;
    --dark:#2b2b2b;
    --text:#4a4a4c;
    --white:#ffffff;
    --bg-light:#f7f7f7;
    --bg-mid:#ececec;
  }
  *{box-sizing:border-box;margin:0;padding:0}
  html,body{width:1200px;height:1003px;overflow:hidden;background:var(--white)}
  body{position:relative;font-family:"Roboto",sans-serif;color:var(--text)}

  .header{position:absolute;left:0;top:0;width:1200px;height:165px;background:var(--white)}
  .brand{position:absolute;left:40px;top:110px;display:flex;align-items:center;gap:10px}
  .brand-mark{width:22px;height:22px;border-radius:50%;background:var(--orange)}
  .brand-name{font-family:"Roboto",sans-serif;font-weight:500;font-size:22px;line-height:1;color:var(--text)}
  .band{position:absolute;left:0;top:0;width:1200px;height:154px;
    background:linear-gradient(90deg,var(--orange-deep) 20%,var(--orange) 65%,var(--orange-deep) 100%);
    clip-path:polygon(279px 0,1200px 0,1200px 154px,367px 154px)}
  .title{position:absolute;left:372px;top:24px;font-family:"Roboto Condensed",sans-serif;font-weight:700;font-size:58px;line-height:58px;color:var(--white);letter-spacing:.8px;white-space:nowrap}
  .mission{position:absolute;left:376px;top:90px;font-family:"Roboto Condensed",sans-serif;font-weight:300;font-size:34px;line-height:40px;color:var(--white);white-space:nowrap}
  .rule{position:absolute;left:0;top:163px;width:1200px;height:4px;background:var(--grey)}

  .body{position:absolute;left:0;top:167px;width:1200px;height:836px;background:linear-gradient(160deg,var(--bg-light),var(--bg-mid) 60%,var(--bg-light))}
  .shapes{position:absolute;left:0;top:0;width:1200px;height:1003px}

  .core{position:absolute;left:98px;top:432px;width:296px;text-align:center;--c:var(--orange)}
  .core h2{font-weight:500;font-size:20px;line-height:26px;color:var(--text)}
  .core p{margin-top:6px;font-size:15px;line-height:19.7px;text-align:justify;text-align-last:center}
  .core h3{margin-top:12px;font-weight:500;font-size:20px;line-height:26px}
  .core ul{margin:6px 0 0 27px;text-align:left;list-style:none;font-size:16px;line-height:21.5px}

  .tick{display:inline-block;position:relative;width:11px;height:11px;border-radius:50%;background:var(--c);vertical-align:-1px;margin-right:6px}
  .tick::after{content:"";position:absolute;left:3.5px;top:1.8px;width:3px;height:5px;border:solid var(--white);border-width:0 1.6px 1.6px 0;transform:rotate(45deg)}
  .core .tick{width:12px;height:12px;margin-right:8px}
  .core .tick::after{left:4px;top:2px}

  .card{position:absolute;left:732px;width:440px}
  .card h4{font-weight:500;font-size:21px;line-height:24px;color:var(--text);letter-spacing:.2px}
  .card p{margin-top:6px;font-size:12.5px;line-height:16.8px;white-space:nowrap}
  .card ul{margin:6px 0 0 24px;list-style:none;font-size:12.5px;line-height:16.8px}
  .card li{white-space:nowrap}
  .card .wrap{padding-left:17px}
  .supported{top:215px;--c:var(--red)}
  .prepared{top:415px;--c:var(--orange)}
  .prepared ul{line-height:15.5px;margin-top:9px}
  .engaged{top:613px;--c:var(--grey)}
  .wise{top:810px;--c:var(--dark)}
</style>
</head>
<body>
  <header class="header">
    <div class="brand"><span class="brand-mark"></span><span class="brand-name">Brightlane 4 Jobs</span></div>
    <div class="band"></div>
    <h1 class="title">B4J CAREER READINESS MODEL</h1>
    <div class="mission">Our mission is to ensure all students are:</div>
    <div class="rule"></div>
  </header>

  <main class="body"></main>

  <svg class="shapes" viewBox="85 90 1913 1548" preserveAspectRatio="none">
    <defs>
      <radialGradient id="bevel" cx="50%" cy="50%" r="50%">
        <stop offset="88%" stop-color="#f2f2f2"/>
        <stop offset="100%" stop-color="#bdbdbd"/>
      </radialGradient>
      <filter id="soft" x="-20%" y="-20%" width="140%" height="140%">
        <feDropShadow dx="0" dy="6" stdDeviation="10" flood-color="#000" flood-opacity=".18"/>
      </filter>
    </defs>

    <g fill="none" stroke-width="36">
      <path d="M452 604 A372 372 0 0 1 746 717" stroke="#e4430f"/>
      <path d="M746 717 A372 372 0 0 1 850 988" stroke="#f7941d"/>
      <path d="M850 988 A372 372 0 0 1 697 1276" stroke="#58585a"/>
      <path d="M697 1276 A372 372 0 0 1 452 1346" stroke="#2b2b2b"/>
    </g>

    <g fill="none" stroke-width="9">
      <polyline points="640,585 680,540 946,540" stroke="#e4430f"/>
      <line x1="876" y1="855" x2="946" y2="855" stroke="#f7941d"/>
      <line x1="862" y1="1148" x2="946" y2="1148" stroke="#58585a"/>
      <polyline points="612,1370 675,1406 946,1406" stroke="#2b2b2b"/>
    </g>

    <circle cx="478" cy="975" r="324" fill="#fff" filter="url(#soft)"/>
    <circle cx="478" cy="975" r="306" fill="url(#bevel)"/>
    <circle cx="478" cy="975" r="288" fill="#fff" filter="url(#soft)"/>

    <g stroke="#fff" stroke-width="7" font-family="Roboto, sans-serif" font-weight="500" font-size="40" text-anchor="middle">
      <circle cx="618" cy="627" r="33" fill="#e4430f"/>
      <circle cx="832" cy="852" r="33" fill="#f7941d"/>
      <circle cx="820" cy="1140" r="33" fill="#58585a"/>
      <circle cx="585" cy="1333" r="33" fill="#2b2b2b"/>
      <g stroke="none" fill="#fff">
        <text x="618" y="641">1</text>
        <text x="832" y="866">2</text>
        <text x="820" y="1154">3</text>
        <text x="585" y="1347">4</text>
      </g>
    </g>

    <g fill="none" stroke-width="6">
      <path d="M1100 400 H1800 A129 129 0 0 1 1800 658 H1100" stroke="#e4430f"/>
      <path d="M1100 697 H1805 A126 126 0 0 1 1805 950 H1100" stroke="#f7941d"/>
      <path d="M1100 1000 H1812 A118 118 0 0 1 1812 1237 H1100" stroke="#58585a"/>
      <path d="M1100 1310 H1808 A123 123 0 0 1 1808 1556 H1100" stroke="#2b2b2b"/>
    </g>

    <g>
      <circle cx="1102" cy="525" r="137" fill="#fff" filter="url(#soft)"/>
      <circle cx="1102" cy="525" r="118" fill="#e4430f" role="img" aria-label="Icon: one person helping another climb a step"/>
      <circle cx="1102" cy="825" r="137" fill="#fff" filter="url(#soft)"/>
      <circle cx="1102" cy="825" r="118" fill="#f7941d" role="img" aria-label="Icon: graduation cap"/>
      <circle cx="1102" cy="1127" r="137" fill="#fff" filter="url(#soft)"/>
      <circle cx="1102" cy="1127" r="118" fill="#58585a" role="img" aria-label="Icon: handshake"/>
      <circle cx="1102" cy="1432" r="137" fill="#fff" filter="url(#soft)"/>
      <circle cx="1102" cy="1432" r="118" fill="#2b2b2b" role="img" aria-label="Icon: person climbing rising steps"/>
    </g>
  </svg>

  <section class="core">
    <h2>Data-Informed and<br>Evidence-Based Practices</h2>
    <p>Brightlane4Jobs relies on robust labor market data tools and sound educational research to guide our development efforts and encourage the use of informed career readiness practices educational settings.</p>
    <h3>B4J Data Tools</h3>
    <ul>
      <li><span class="tick"></span>Labor Market Data System</li>
      <li><span class="tick"></span>Employer Surveys</li>
      <li><span class="tick"></span>Regional Labor Market Reports</li>
    </ul>
  </section>

  <section class="card supported">
    <h4>CAREER SUPPORTED</h4>
    <p>Students benefit from informed educational leadership and policymaking<br>that result in effective career resources and learning opportunities</p>
    <ul>
      <li><span class="tick"></span>B4J Policy Tools</li>
      <li><span class="tick"></span>Title CTE Technical Support</li>
      <li><span class="tick"></span>Professional Development</li>
      <li><span class="tick"></span>Industry-Education Relationships</li>
    </ul>
  </section>

  <section class="card prepared">
    <h4>CAREER PREPARED</h4>
    <p>Students have the necessary foundational, technical, and workplace<br>skills needed to support success in a variety of careers.</p>
    <ul>
      <li><span class="tick"></span>Career-Focused Curricula</li>
      <li><span class="tick"></span>Math Assessments with Scalar Career Database (powered by the</li>
      <li class="wrap">Scalar<sup style="font-size:7px">®</sup> Framework for Mathematics)</li>
    </ul>
  </section>

  <section class="card engaged">
    <h4>CAREER ENGAGED</h4>
    <p>Students are motivated and inspired to develop career skills and<br>seek employment opportunities that meet both personal and</p>
    <ul>
      <li><span class="tick"></span>Career Awareness &amp; Exposure</li>
      <li><span class="tick"></span>Purposeful Learning Connected to Careers</li>
    </ul>
  </section>

  <section class="card wise">
    <h4>CAREER WISE</h4>
    <p>Students have insight into personal values and interests, as well as<br>the economic realities of the job market, that supports informed</p>
    <ul>
      <li><span class="tick"></span>Career Pathways</li>
      <li><span class="tick"></span>Career Exploration</li>
      <li><span class="tick"></span>Educator Career Guides</li>
    </ul>
  </section>
</body>
</html>
```